依頼詳細
サイトの特徴としては東京都内の賃料15万円以上のマンションを中心に掲載しているサイトになります。

高級感、安心感のあるバナーを希望します。
バナーからのリンクはサイトトップページに遷移させます。
サイト:邸宅彩館 https://www.teisai-k.com/
サイト特徴説明: https://www.teisai-k.com/visiter

記載項目
素材は特にありませんので、ご提案いただけると幸いです。
記載したい文言は以下です。サイト名は必須でお願いします。
それ以外は必須ではありません。

サイト名:高級賃貸の邸宅彩館

高級賃貸を賢く探すなら
都心の高級賃貸検索サイト
仲介料が最大無料の高級賃貸検索サイト

サイズ
• 300 x 250 ( ミディアムレクタングル )
• 250 x 250 ( スクエアポップアップ )
• 160 x 600 ( ワイドスカイスクレイパー )
• 160×600 468×60  320×50  320×100
希望イメージ
シンプル 複雑
単色 カラフル
暗い 明るい
日常 高級
遊び心 厳粛
未来的 伝統的
女性的 男性的
希望する色
茶系
納品ファイル
補足説明

デザイン性、サイト特徴の訴求性、バランスの3点で各評価の一番高いもの、
総合で良かった2点を当選させて頂きました。
社内でアンケートを取りまして、結果5件を採用とさせていただきました。

たくさんのご提案をいただきまして、誠にありがとうございました。
みなさま素晴らしいご提案ばかりで、とても迷いました。
採用できなかった方へは大変心苦しいですが、こちらで募集をしてよかったです。
また機会がございましたら、ぜひよろしくお願いいたします。

```html
<!DOCTYPE html>
<html lang="ja">
<head>
<meta charset="UTF-8">
<title>高級賃貸の邸宅彩館 バナー</title>
<link rel="stylesheet" href="https://fonts.googleapis.com/css2?family=Shippori+Mincho:wght@500;700;800&display=swap">
<style>
  :root {
    --brown-deep: #241612;
    --brown-mid: #35221c;
    --night-top: #0f1a3a;
    --night-mid: #1a2240;
    --city-warm: #4a3a30;
    --white: #ffffff;
    --badge-bg: rgba(255, 255, 255, 0.88);
    --ink: #1c1412;
    --button: #b0554f;
    --button-edge: #8e3d39;
  }
  * { margin: 0; padding: 0; box-sizing: border-box; }
  html, body { width: 1200px; height: 4500px; overflow: hidden; }
  body { background: var(--brown-deep); font-family: "Shippori Mincho", serif; }
  .banner { position: relative; width: 1200px; height: 4500px; overflow: hidden; background: var(--brown-deep); }

  .header {
    position: absolute; left: 0; top: 0; width: 1200px; height: 980px;
    background: linear-gradient(180deg, var(--brown-mid), var(--brown-deep));
  }
  .site-title {
    position: absolute; left: 0; width: 100%; text-align: center;
    color: var(--white); font-weight: 700; line-height: 1; white-space: nowrap;
  }
  .site-title .line-1 { position: absolute; top: 250px; left: 0; width: 100%; font-size: 210px; letter-spacing: 4px; }
  .site-title .line-2 { position: absolute; top: 560px; left: 0; width: 100%; font-size: 220px; letter-spacing: 8px; }

  .cityscape {
    position: absolute; left: 0; top: 980px; width: 1200px; height: 2920px;
    background:
      radial-gradient(ellipse 900px 700px at 60% 70%, rgba(210,150,90,0.35), transparent 70%),
      linear-gradient(180deg, var(--night-top) 0%, var(--night-mid) 30%, var(--city-warm) 65%, #2b2630 100%);
  }
  .tagline {
    position: absolute; left: 0; width: 100%; text-align: center;
    color: var(--white); font-weight: 800; line-height: 1; white-space: nowrap;
    text-shadow: 0 0 24px rgba(120,160,255,0.8), 0 0 8px rgba(255,255,255,0.6);
  }
  .tagline .line-1 { position: absolute; top: 1125px; left: 0; width: 100%; font-size: 134px; }
  .tagline .line-2 { position: absolute; top: 1395px; left: 0; width: 100%; font-size: 134px; letter-spacing: 6px; }

  .fee-badge {
    position: absolute; left: 190px; top: 2840px; width: 840px; height: 840px;
    border-radius: 50%; background: var(--badge-bg);
    box-shadow: 0 0 0 10px rgba(255,255,255,0.35);
    color: var(--ink); text-align: center; font-weight: 700; white-space: nowrap;
  }
  .fee-badge .label {
    position: absolute; top: 225px; left: 0; width: 100%;
    font-size: 150px; line-height: 1; letter-spacing: 4px;
  }
  .fee-badge .value {
    position: absolute; top: 420px; left: 0; width: 100%; height: 230px;
    display: flex; justify-content: center; align-items: baseline;
    line-height: 1; font-size: 140px;
  }
  .fee-badge .value .accent { font-size: 220px; font-weight: 800; }

  .footer {
    position: absolute; left: 0; top: 3900px; width: 1200px; height: 600px;
    background: var(--brown-deep);
  }
  .cta-button {
    position: absolute; left: 88px; top: 4000px; width: 1012px; height: 412px;
    background: var(--button); border: 6px solid var(--button-edge);
    color: var(--white); text-decoration: none;
  }
  .cta-button .cta-text {
    position: absolute; left: 120px; top: 58px; font-size: 144px; font-weight: 700; line-height: 1.2; white-space: nowrap;
  }
  .cta-button .cta-arrow { position: absolute; left: 800px; top: 136px; width: 120px; height: 140px; }
</style>
</head>
<body>
  <div class="banner">
    <header class="header">
      <h1 class="site-title">
        <span class="line-1">高級賃貸の</span>
        <span class="line-2">邸宅彩館</span>
      </h1>
    </header>

    <div class="cityscape" role="img" aria-label="東京都心の夜景、高層ビル群とライトアップされたタワー"></div>

    <p class="tagline">
      <span class="line-1">都心の高級賃貸を</span>
      <span class="line-2">賢く探す</span>
    </p>

    <div class="fee-badge">
      <span class="label">仲介料</span>
      <span class="value"><span>最大</span><span class="accent">無料</span></span>
    </div>

    <div class="footer"></div>
    <a class="cta-button" href="https://www.teisai-k.com/">
      <span class="cta-text">詳しくは<br>こちら</span>
      <svg class="cta-arrow" viewBox="0 0 120 140" aria-hidden="true">
        <polygon points="0,0 120,70 0,140" fill="#ffffff"/>
      </svg>
    </a>
  </div>
</body>
</html>
```